IT services company requires Letterhead design

We need a professional letterhead designed to be used for general correspondence with customers, quotes, invoices etc. We are a new IT services company specialising in computer servicing and repairs and mobile and tablet repairs. Attached are templates that my printing company have supplied, my logos, an interpretation of our website for you to get a feel of the company. Details to be included on the letterhead are

Company Number – 4738261
VAT Number - 518337942
Registered Address – 14-16 Brambly Lane, London, E4 9QT

Phone – 01632 487215
Email – sales@quorvent.com
Web – www.quorvent.com

I would prefer for the top of the letterhead to just have the company logo on a white background and the rest of the details on the bottom of the letterhead but I am open to design ideas.

Thanks

```html
<!DOCTYPE html>
<html lang="en">
<head>
<meta charset="utf-8">
<title>Quorvent Letterhead</title>
<link href="https://fonts.googleapis.com/css2?family=Open+Sans:wght@400;700&display=swap" rel="stylesheet">
<style>
  :root {
    --brand-blue: #2fc1e1;
    --ink-dark: #3a3a3c;
    --paper: #ffffff;
  }
  html, body {
    margin: 0;
    padding: 0;
    overflow: hidden;
    background: var(--paper);
  }
  .letterhead {
    position: relative;
    width: 855px;
    height: 1200px;
    overflow: hidden;
    background: var(--paper);
    font-family: "Open Sans", Arial, sans-serif;
  }
  .brand {
    position: absolute;
    left: 62px;
    top: 92px;
    display: flex;
    align-items: center;
    gap: 10px;
  }
  .brand-square {
    width: 22px;
    height: 22px;
    background: var(--brand-blue);
  }
  .brand-name {
    font-size: 34px;
    font-weight: 700;
    color: var(--ink-dark);
    letter-spacing: -0.5px;
  }
  .sidebar {
    position: absolute;
    left: 0;
    top: 225px;
    width: 234px;
    height: 975px;
  }
  .contact {
    position: absolute;
    left: 0;
    width: 234px;
    color: var(--paper);
    font-size: 15.5px;
    line-height: 22px;
  }
  .contact-item {
    position: absolute;
    left: 41px;
    display: flex;
    align-items: flex-start;
    gap: 10px;
    white-space: nowrap;
  }
  .contact-icon {
    width: 15px;
    height: 15px;
    margin-top: 3px;
    flex: none;
  }
  .vat-number {
    position: absolute;
    left: 41px;
    font-size: 12.5px;
    white-space: nowrap;
  }
</style>
</head>
<body>
<div class="letterhead">

  <div class="brand">
    <span class="brand-square"></span>
    <span class="brand-name">Quorvent</span>
  </div>

  <svg class="sidebar" viewBox="0 0 234 975" width="234" height="975" aria-hidden="true">
    <path d="M0 0 H178 V54 H234 V975 H0 Z" fill="var(--brand-blue)"/>
    <rect x="115" y="54" width="35" height="32" fill="var(--paper)"/>
    <rect x="168" y="94" width="35" height="31" fill="var(--paper)"/>
  </svg>

  <div class="contact">
    <div class="contact-item" style="top:1025px">
      <svg class="contact-icon" viewBox="0 0 16 16" aria-hidden="true">
        <path d="M8 2 L15 8.5 H13 V14 H9.5 V10 H6.5 V14 H3 V8.5 H1 Z" fill="#fff"/>
      </svg>
      <span>14-16 Brambly Lane,<br>London, E4 9QT</span>
    </div>
    <div class="contact-item" style="top:1075px">
      <svg class="contact-icon" viewBox="0 0 16 16" aria-hidden="true">
        <path d="M4 1.5 L6.3 4.5 L5 6.2 C5.8 8 7.6 9.9 9.6 11 L11.3 9.7 L14.3 12 L12.6 14.4 C7.4 13.8 2.4 8.8 1.8 3.4 Z" fill="#fff"/>
      </svg>
      <span>01632 487215</span>
    </div>
    <div class="contact-item" style="top:1103px">
      <svg class="contact-icon" viewBox="0 0 16 16" aria-hidden="true">
        <circle cx="8" cy="8" r="2.6" fill="none" stroke="#fff" stroke-width="1.8"/>
        <path d="M10.6 5.5 V9.3 C10.6 11 13.8 11 13.8 8 A5.8 5.8 0 1 0 11.2 12.8" fill="none" stroke="#fff" stroke-width="1.8"/>
      </svg>
      <span>alex@quorvent.com</span>
    </div>
    <div class="contact-item" style="top:1132px">
      <svg class="contact-icon" viewBox="0 0 16 16" aria-hidden="true">
        <g fill="none" stroke="#fff" stroke-width="1.3">
          <circle cx="8" cy="8" r="6.3"/>
          <ellipse cx="8" cy="8" rx="2.7" ry="6.3"/>
          <path d="M1.7 8 H14.3 M2.8 4.7 H13.2 M2.8 11.3 H13.2"/>
        </g>
      </svg>
      <span>www.quorvent.com</span>
    </div>
    <div class="vat-number" style="top:1172px">VAT Number - 518337942</div>
  </div>

</div>
</body>
</html>
```